PPT Design Project for an educational startup

We seek a PPT design for a new company based in Japan called "Brevonta".
We provide PPT slide-based educational videos for free.
Please see the link below. You will see some videos.
http://marvex-example.jp/
The current template is also attached.
As we are changing our service name from Marvex to Brevonta, we are considering to change the PPT template as well.
Here are some notes regarding this project.
1. We need three pages;
- Title page: Letters for the tile and the logo are necessary. Some pictorial marks or other design would be appreciated.
- Contents page: Just one line to divide the message part and contents part should be sufficient. Please do not spend your time here.
- Final page: The word "Thank you for watching!" in the center. Some pictorial marks or other design would be appreciated.
2. Please use light green, orange, and purple as main colors. (Same as the current template)
3. You don't have to think about the font-style. This is going to be Japanese font, so we will take care of this.
4. Background color needs to be white, as the slides could be printed out.
5. We use Powerpoint for Mac.
6. No copyright section required, as these slides will be creative commons. Instead of the copyright section, please put the creative commons mark in all slides. (which is in the original template attached)
Updates
Please forget about the creative commons mark.
Hi all,
Target Market(s)
16-25 years old people, who are highly educated or highly motivated for education
Industry/Entity Type
It Company
Requirements
Must have
- 1. Creative commons mark (which is in the original template)
Should not have
- 1. Copyright mark

```html
<!DOCTYPE html>
<html lang="en">
<head>
<meta charset="utf-8">
<title>Brevonta presentation template</title>
<link rel="stylesheet" href="https://fonts.googleapis.com/css2?family=Carlito:wght@400;700&family=Chewy&display=swap">
<style>
  :root {
    --green: #7dbb2f;
    --lime: #b5cc1e;
    --olive: #9aa51a;
    --orange: #ef7d1a;
    --purple: #7d5aa6;
    --ink: #1e1e1e;
    --paper: #ffffff;
    --canvas: #ffffff;
    --green-soft: rgba(125,187,47,.75);
    --lime-soft: rgba(181,204,30,.8);
    --purple-soft: rgba(125,90,166,.55);
    --orange-soft: rgba(239,125,26,.55);
    --clear: rgba(255,255,255,0);
  }
  * { box-sizing: border-box; margin: 0; padding: 0; }
  html, body { width: 1200px; height: 329px; overflow: hidden; background: var(--canvas); }
  body { position: relative; font-family: "Carlito", "Calibri", Arial, sans-serif; color: var(--ink); }

  .slide {
    position: absolute; top: 50px; height: 247px; background: var(--paper);
    box-shadow: 1px 2px 4px rgba(0,0,0,.45); overflow: hidden;
  }
  .slide--title { left: 33px; width: 328px; }
  .slide--content { left: 434px; width: 331px; }
  .slide--closing { left: 824px; width: 328px; }

  .brand { position: absolute; color: var(--green); font-weight: 700; letter-spacing: -.2px; }
  .decor { position: absolute; }

  /* Title slide */
  .slide--title .brand { left: 19px; top: 30px; font-size: 18px; }
  .slide--title .decor--top { right: -20px; top: -20px; width: 150px; height: 150px;
    background:
      radial-gradient(closest-side at 55% 45%, var(--lime-soft), var(--clear)),
      radial-gradient(closest-side at 75% 70%, var(--purple-soft), var(--clear)),
      radial-gradient(closest-side at 30% 40%, var(--orange-soft), var(--clear)); }
  .slide--title .decor--bottom { left: -14px; bottom: -14px; width: 76px; height: 76px;
    background:
      radial-gradient(closest-side at 50% 50%, var(--green-soft), var(--clear)),
      radial-gradient(closest-side at 35% 35%, var(--purple-soft), var(--clear)); }
  .title-heading { position: absolute; left: 19px; top: 89px; width: 160px;
    color: var(--green); font-size: 17px; font-weight: 400; line-height: 1.25; }
  .title-subtitle { position: absolute; right: 21px; top: 187px; width: 150px; text-align: right;
    font-size: 11px; line-height: 1.3; }

  /* Content slide */
  .content-heading { position: absolute; left: 15px; top: 12px; color: var(--green); font-size: 16px; font-weight: 400; }
  .content-rule { position: absolute; left: 11px; top: 38px; width: 290px; border-top: 1.5px dotted var(--lime); }
  .slide--content .decor--top { right: -12px; top: -12px; width: 58px; height: 62px;
    background:
      radial-gradient(closest-side at 50% 50%, var(--lime-soft), var(--clear)),
      radial-gradient(closest-side at 40% 60%, var(--purple-soft), var(--clear)); }
  .slide--content .decor--bottom { left: -12px; bottom: -12px; width: 50px; height: 60px;
    background:
      radial-gradient(closest-side at 50% 50%, var(--green-soft), var(--clear)),
      radial-gradient(closest-side at 60% 35%, var(--orange-soft), var(--clear)); }
  .bullets { position: absolute; left: 13px; top: 46px; width: 300px; list-style: none; font-size: 10.3px; line-height: 1.2; }
  .bullets > li { position: relative; padding-left: 14px; margin-bottom: 4px; }
  .bullets > li::before { content: ""; position: absolute; left: 2px; top: 3px; width: 4px; height: 4px; background: var(--orange); }
  .bullets ul { list-style: none; margin-top: 6px; font-size: 7.8px; }
  .bullets ul li { position: relative; padding-left: 14px; margin-bottom: 5px; }
  .bullets ul li::before { content: "–"; position: absolute; left: 2px; top: 0; color: var(--orange); }
  .footer-date { position: absolute; left: 49px; bottom: 10px; color: var(--orange); font-size: 5.5px; }
  .footer-page { position: absolute; left: 256px; bottom: 10px; color: var(--orange); font-size: 5.5px; }
  .slide--content .brand { left: 278px; bottom: 7px; font-size: 9px; }

  /* Closing slide */
  .slide--closing .decor--left { left: 0; top: 30px; width: 130px; height: 180px;
    background:
      radial-gradient(closest-side at 55% 50%, var(--green-soft), var(--clear)),
      radial-gradient(closest-side at 70% 25%, var(--purple-soft), var(--clear)),
      radial-gradient(closest-side at 25% 70%, var(--orange-soft), var(--clear)); }
  .slide--closing .decor--right { left: 180px; top: 20px; width: 148px; height: 180px;
    background:
      radial-gradient(closest-side at 50% 45%, var(--lime-soft), var(--clear)),
      radial-gradient(closest-side at 40% 75%, var(--purple-soft), var(--clear)),
      radial-gradient(closest-side at 80% 20%, var(--orange-soft), var(--clear)); }
  .thanks-banner { position: absolute; left: 81px; top: 90px; width: 166px; height: 64px;
    background: linear-gradient(100deg, var(--olive), var(--lime));
    box-shadow: 0 3px 5px rgba(0,0,0,.25);
    display: flex; align-items: center; justify-content: center; text-align: center; }
  .thanks-text { font-family: "Chewy", "Comic Sans MS", cursive; color: #fff; font-size: 18px; line-height: 1.1; letter-spacing: .5px; }
  .slide--closing .brand { right: 18px; bottom: 10px; font-size: 9px; }
</style>
</head>
<body>

<section class="slide slide--title" aria-label="Title slide">
  <div class="decor decor--top" role="img" aria-label="Cluster of overlapping green, orange and purple squares"></div>
  <div class="decor decor--bottom" role="img" aria-label="Small cluster of green, orange and purple squares"></div>
  <div class="brand">Brevonta</div>
  <h1 class="title-heading">Lorem ipsum dolor sit amet</h1>
  <p class="title-subtitle">Ut commodo leo a ligula dignissim ullamcorper</p>
</section>

<section class="slide slide--content" aria-label="Contents slide">
  <div class="decor decor--top" role="img" aria-label="Small cluster of coloured squares"></div>
  <div class="decor decor--bottom" role="img" aria-label="Small cluster of coloured squares"></div>
  <h2 class="content-heading">Lorem ipsum dolor sit amet</h2>
  <div class="content-rule"></div>
  <ul class="bullets">
    <li>Lorem ipsum dolor sit amet, consectetur adipiscing elit. Suspendisse eget commodo ipsum.</li>
    <li>Phasellus ligula augue, iaculis ut adipiscing pulvinar, laoreet in elit. Vivamus ullamcorper eros tristique lacus mattis dapibus.</li>
    <li>Ut commodo leo a ligula dignissim ullamcorper. Aliquam tempus nunc nec lorem vulputate sollicitudin.
      <ul>
        <li>Fusce rutrum gravida quam nec tristique.</li>
        <li>Nulla vulputate metus eget turpis tempor vehicula. Aliquam blandit diam at turpis interdum vestibulum.</li>
      </ul>
    </li>
    <li>Duis turpis sapien, laoreet quis egestas non, semper sed justo. Vestibulum vitae rhoncus enim.</li>
  </ul>
  <span class="footer-date">15-Dec-12</span>
  <span class="footer-page">2</span>
  <div class="brand">Brevonta</div>
</section>

<section class="slide slide--closing" aria-label="Closing slide">
  <div class="decor decor--left" role="img" aria-label="Cluster of floating green, orange and purple squares"></div>
  <div class="decor decor--right" role="img" aria-label="Cluster of floating green, orange and purple squares"></div>
  <div class="thanks-banner">
    <p class="thanks-text">Thank you<br>for watching!</p>
  </div>
  <div class="brand">Brevonta</div>
</section>

</body>
</html>
```